Calvin Hobbs International Country Singer

We need a Cd cover for Calvin Hobbs. The title is "Ride The Dust". Really looking for a fresh innovative look at days gone by. Fairly standard brief as far as cd cover's are concerned. looking for a catchy flow through the booklet. Images are available of the artist, more for inside the booklet than for use on the cover.
New CD title: Ride The Dust
Artist name: Calvin Hobbs
Current website: CalvinHobbs.com
Facebook: facebook.com/CalvinHobbs

Industry/Entity Type

Singer

Logo Text

Calvin Hobbs Ride The Dust

Font styles to use
Decorative

```html
<!DOCTYPE html>
<html lang="en">
<head>
<meta charset="utf-8">
<title>Calvin Hobbs – Ride The Dust</title>
<link rel="stylesheet" href="https://fonts.googleapis.com/css2?family=Rye&family=Poiret+One&display=swap">
<style>
  :root {
    --wood-dark: #2e1a10;
    --wood-mid: #4a2a18;
    --wood-light: #5c3620;
    --soundhole-rim: #24140d;
    --soundhole: #0f0907;
    --rosette-gold: #b07a32;
    --rosette-dark: #1c1410;
    --heart-red: #c23a2a;
    --heart-deep: #6e1c14;
    --cream: #e0d3b8;
    --string: #f4efe6;
  }
  html, body {
    margin: 0;
    padding: 0;
    overflow: hidden;
    background: var(--wood-dark);
  }
  .cover {
    position: relative;
    width: 1200px;
    height: 1200px;
    overflow: hidden;
  }
  .cover__art {
    position: absolute;
    inset: 0;
    width: 1200px;
    height: 1200px;
  }
  .title {
    font-family: "Rye", serif;
    fill: var(--cream);
  }
  .artist-name {
    font-family: "Poiret One", sans-serif;
    fill: var(--cream);
  }
  .guitar-string {
    stroke: var(--string);
    stroke-width: 2.4;
  }
</style>
</head>
<body>
<main class="cover">
  <svg class="cover__art" viewBox="0 0 1200 1200" xmlns="http://www.w3.org/2000/svg">
    <defs>
      <linearGradient id="wood-grain" x1="0" y1="0" x2="1" y2="0">
        <stop offset="0" stop-color="var(--wood-mid)"/>
        <stop offset="0.5" stop-color="var(--wood-light)"/>
        <stop offset="1" stop-color="var(--wood-mid)"/>
      </linearGradient>
      <radialGradient id="centre-tone" cx="0.5" cy="0.5" r="0.5">
        <stop offset="0" stop-color="var(--heart-red)"/>
        <stop offset="0.65" stop-color="var(--heart-deep)"/>
        <stop offset="1" stop-color="var(--soundhole)"/>
      </radialGradient>
    </defs>

    <rect class="guitar-top" width="1200" height="1200" fill="url(#wood-grain)"
          role="img" aria-label="Dark wood grain of an acoustic guitar top"/>

    <g class="soundhole">
      <circle cx="600" cy="608" r="552" fill="var(--soundhole-rim)"/>
      <circle cx="600" cy="608" r="498" fill="var(--rosette-gold)"/>
      <circle cx="600" cy="608" r="490" fill="var(--rosette-dark)"/>
      <circle cx="600" cy="608" r="462" fill="var(--rosette-gold)"/>
      <circle cx="600" cy="608" r="456" fill="var(--rosette-dark)"/>
      <circle cx="600" cy="608" r="438" fill="var(--rosette-gold)"/>
      <circle cx="600" cy="608" r="432" fill="var(--soundhole)"/>
    </g>

    <circle class="centre-illustration" cx="600" cy="608" r="432" fill="url(#centre-tone)"
            role="img" aria-label="Illustration of an anatomical red heart inside the soundhole"/>

    <g class="title-block">
      <text class="title title--small" x="586" y="592" text-anchor="middle"
            font-size="265" textLength="620" lengthAdjust="spacingAndGlyphs">RIDE THE</text>
      <text class="title title--large" x="616" y="928" text-anchor="middle"
            font-size="430" textLength="912" lengthAdjust="spacingAndGlyphs">DUST</text>
    </g>

    <g class="strings">
      <line class="guitar-string" x1="404" y1="0" x2="404" y2="1200"/>
      <line class="guitar-string" x1="484" y1="0" x2="484" y2="1200"/>
      <line class="guitar-string" x1="568" y1="0" x2="568" y2="1200"/>
      <line class="guitar-string" x1="628" y1="0" x2="628" y2="1200"/>
      <line class="guitar-string" x1="708" y1="0" x2="708" y2="1200"/>
      <line class="guitar-string" x1="780" y1="0" x2="780" y2="1200"/>
    </g>

    <g class="artist">
      <text class="artist-name" x="1176" y="1096" text-anchor="end" font-size="74"
            textLength="284" lengthAdjust="spacingAndGlyphs">CALVIN</text>
      <text class="artist-name" x="1176" y="1146" text-anchor="end" font-size="54"
            textLength="284" lengthAdjust="spacingAndGlyphs">HOBBS</text>
    </g>
  </svg>
</main>
</body>
</html>
```